Website Re-Design

We would like to explore the possibility of a re-design of our website. We want all the content that it currently has to remain on the pages, and we don't want our logo/corporate identity or colours changed, so it is literally just a website re-design.

Our website is www.trovalink.co.uk

Websites that we like are

http://www.quillmarsh.co.uk/
http://rankwidget.com/

```html
<!DOCTYPE html>
<html lang="en">
<head>
<meta charset="utf-8">
<title>Trovalink – Inbound Marketing &amp; SEO Performance Agency</title>
<link href="https://fonts.googleapis.com/css2?family=Oswald:wght@300;400;500&family=Open+Sans:wght@400;600;700&display=swap" rel="stylesheet">
<style>
:root{
  --pink:#e2167e;
  --green:#86c142;
  --green-dark:#6fae2e;
  --teal:#13a594;
  --teal-dark:#0f8f80;
  --teal-deep:#0c7d70;
  --grey-bar:#ececec;
  --grey-light:#f1f1f1;
  --ink:#2b2b2b;
  --muted:#555;
  --white:#fff;
}
*{box-sizing:border-box;margin:0;padding:0}
html,body{width:1200px;height:3504px;overflow:hidden}
body{font-family:"Open Sans",Arial,sans-serif;color:var(--ink);background:var(--white);font-size:15px;line-height:1.5}
.wrap{width:920px;margin:0 auto;position:relative}
.heading{font-family:"Oswald",Arial,sans-serif;font-weight:400;text-transform:uppercase}

/* top bar */
.topbar{height:28px;background:var(--grey-bar);font-size:12px;color:var(--muted)}
.topbar .wrap{display:flex;justify-content:flex-end;gap:26px;align-items:center;height:28px}
.topbar span{display:flex;align-items:center;gap:6px}

/* header */
.site-header{height:88px}
.site-header .wrap{display:flex;justify-content:space-between;align-items:center;height:88px}
.brand{font-family:"Oswald",Arial,sans-serif;font-weight:500;font-size:34px;letter-spacing:2px;color:var(--pink);display:flex;align-items:center;gap:10px}
.brand i{width:14px;height:14px;background:var(--green);border-radius:50%;display:block}
.nav{display:flex;gap:34px}
.nav a{font-family:"Oswald",Arial,sans-serif;font-weight:300;font-size:24px;color:var(--teal);text-decoration:none;text-transform:uppercase;padding:4px 0}
.nav a.active{border-bottom:2px solid var(--teal)}

/* hero */
.hero-visual{height:556px;background:linear-gradient(180deg,#4f6f8f 0%,#9fb5c8 45%,#e5e9ed 100%)}

/* intro band */
.intro{height:315px;background:linear-gradient(180deg,var(--green-dark),var(--green));color:var(--white);text-align:center;position:relative}
.intro h1{padding-top:76px;font-size:36px;letter-spacing:3px;font-weight:400}
.intro p{width:880px;margin:28px auto 0;font-size:15px;line-height:1.55}
.chevron{position:absolute;left:50%;bottom:-17px;margin-left:-17px;width:34px;height:34px}

/* services */
.services{height:553px;padding-top:68px}
.services .wrap{display:flex}
.service{flex:1;padding:0 22px;border-left:1px solid #ddd}
.service:first-child{padding-left:0;border-left:0}
.service h2{font-size:22px;letter-spacing:.5px;padding-bottom:12px;border-bottom:1px solid #ddd}
.service .art{height:190px;margin:20px 0 24px}
.service p{font-size:15px;line-height:1.5;height:88px;color:var(--ink)}
.btn{display:inline-block;background:var(--teal);color:var(--white);font-size:13px;text-transform:uppercase;padding:9px 22px;text-decoration:none}

/* recent works */
.works{height:557px;background:linear-gradient(135deg,#e4e4e4,#f4f4f4 40%,#e8e8e8 70%,#f2f2f2);text-align:center;position:relative;padding-top:96px}
.label{font-size:13px;font-weight:700;letter-spacing:2px;text-transform:uppercase}
.works .label{color:var(--pink)}
.works p{width:820px;margin:18px auto 0;font-size:15px}
.thumbs{display:flex;gap:8px;margin-top:42px}
.thumbs div{flex:1;height:186px}

/* clients */
.clients{height:421px;background:linear-gradient(135deg,var(--teal-dark),var(--teal) 50%,var(--teal-dark));color:var(--white);text-align:center;padding-top:100px;position:relative}
.clients p{width:820px;margin:16px auto 0;font-size:15px}
.logos{display:flex;gap:14px;margin-top:48px}
.logo-tile{flex:1;height:106px;background:var(--white);display:flex;align-items:center;justify-content:center;gap:8px;font-weight:700;font-size:18px;color:var(--teal-deep)}
.logo-tile i{width:12px;height:12px;border-radius:50%;background:var(--teal-deep);display:block}

/* cta */
.cta{height:402px;text-align:center;padding-top:96px}
.cta .label{color:var(--pink)}
.cta h2{font-size:30px;font-weight:600;margin-top:40px}
.cta p{width:760px;margin:16px auto 0;font-size:15px}
.cta .btn{margin-top:32px;font-size:16px;padding:14px 28px}

/* contact */
.contact{height:526px;background:var(--teal);color:var(--white);position:relative;padding-top:54px}
.contact .label{text-align:center;display:block}
.contact h2{text-align:center;font-size:54px;font-weight:300;letter-spacing:5px;margin-top:8px}
.contact .lede{text-align:center;width:780px;margin:10px auto 0;font-size:13px;opacity:.85}
.grid{display:grid;grid-template-columns:260px 230px 230px 200px;margin-top:30px;border-top:1px solid rgba(255,255,255,.25)}
.grid > div{padding:14px 0 0 0;border-bottom:1px solid rgba(255,255,255,.25);min-height:112px}
.grid h3{font-size:12px;font-weight:700;text-transform:uppercase;letter-spacing:.5px;margin-bottom:10px}
.grid .val{font-size:17px}
.grid .small{font-size:12px;line-height:1.6}
.grid ul{list-style:none;font-size:12px;line-height:1.75;text-transform:uppercase}
.social{display:flex;gap:12px}
.social i{width:22px;height:22px;border-radius:50%;background:rgba(255,255,255,.85);display:block}
.search input{width:200px;height:30px;border:0;padding:0 10px;font-size:12px}
.search .btn{margin-top:8px;background:var(--teal-deep);padding:6px 16px;font-size:12px}

/* footer */
.site-footer{height:58px;background:var(--teal-deep);color:var(--white)}
.site-footer .wrap{display:flex;align-items:center;gap:40px;height:58px}
.site-footer .brand{color:var(--white);font-size:26px;opacity:.5}
.site-footer p{font-size:11px;line-height:1.5}
</style>
</head>
<body>

<div class="topbar"><div class="wrap">
  <span><svg width="14" height="10" viewBox="0 0 14 10"><rect x=".5" y=".5" width="13" height="9" fill="none" stroke="#555"/><path d="M.5 .5 7 6 13.5 .5" fill="none" stroke="#555"/></svg>HELLO@TROVALINK.CO.UK</span>
  <span><svg width="12" height="12" viewBox="0 0 24 24"><path fill="#555" d="M6.6 10.8a15 15 0 0 0 6.6 6.6l2.2-2.2c.3-.3.7-.4 1-.2 1.1.4 2.3.6 3.6.6.6 0 1 .4 1 1V20c0 .6-.4 1-1 1A17 17 0 0 1 3 4c0-.6.4-1 1-1h3.5c.6 0 1 .4 1 1 0 1.3.2 2.5.6 3.6.1.3 0 .7-.2 1z"/></svg>+44 (0) 20 7946 0321</span>
</div></div>

<header class="site-header"><div class="wrap">
  <div class="brand"><i></i>TROVALINK</div>
  <nav class="nav">
    <a class="active" href="#">Home</a><a href="#">About</a><a href="#">Portfolio</a><a href="#">What we do</a><a href="#">Contact us</a>
  </nav>
</div></header>

<div class="hero-visual" role="img" aria-label="Laptop, phone and tablet on a desk showing the search, social and media services"></div>

<section class="intro">
  <h1 class="heading">Trovalink - Your inbound marketing &amp; SEO performance agency</h1>
  <p>Do you want to earn your customers attention? Gain more visibility in the SERPs and build &amp; engage with your audience? Trovalink specialises in SEO, Social media, CRO and Design &amp; Creative services. Offering a bespoke and personal service from a team of digital natives.</p>
  <svg class="chevron" viewBox="0 0 34 34"><circle cx="17" cy="17" r="16" fill="#fff" stroke="#86c142" stroke-width="2"/><path d="M11 14l6 6 6-6" fill="none" stroke="#86c142" stroke-width="2.5"/></svg>
</section>

<section class="services"><div class="wrap">
  <article class="service">
    <h2 class="heading">What can we do for you?</h2>
    <div class="art" role="img" aria-label="Laptop showing a bar chart" style="background:linear-gradient(180deg,#f4f4f4,#d9d9d9)"></div>
    <p>We offer a bespoke service and will customise to your needs. We specialise in progressive &amp; innovative solutions.</p>
    <a class="btn" href="#">Read more</a>
  </article>
  <article class="service">
    <h2 class="heading">See our portfolio</h2>
    <div class="art" role="img" aria-label="Watering can over a young plant" style="background:linear-gradient(180deg,#f6f6f6,#e4ecd6)"></div>
    <p>Take a look at our case-studies to see our recent campaigns showing results achieved for our clients.</p>
    <a class="btn" href="#">Read more</a>
  </article>
  <article class="service">
    <h2 class="heading">Let's talk</h2>
    <div class="art" role="img" aria-label="Teal rotary telephone" style="background:linear-gradient(180deg,#f6f6f6,#cfe9e5)"></div>
    <p>Use our form to send us a message, we will call you back as soon as we can.</p>
    <a class="btn" href="#">Read more</a>
  </article>
</div></section>

<section class="works"><div class="wrap">
  <div class="label">Recent works</div>
  <p>Check out our recent works and case-studies. These are a few examples to show the diversity of work that we can do to earn real attention, generate inbound links, mentions, citations and be used across many of our marketing channels. See more on our portfolio page and learn about what we could do for you.</p>
  <div class="thumbs">
    <div role="img" aria-label="Website project on laptop screens" style="background:linear-gradient(135deg,#5fb0d8,#e8e0c8)"></div>
    <div role="img" aria-label="Website project on desktop monitors" style="background:linear-gradient(135deg,#3a4a5c,#c9d3dc)"></div>
    <div role="img" aria-label="Magazine app project on tablets" style="background:linear-gradient(135deg,#e85aa6,#7a8fa8)"></div>
  </div>
</div>
<svg class="chevron" viewBox="0 0 34 34"><circle cx="17" cy="17" r="16" fill="#fff" stroke="#13a594" stroke-width="2"/><path d="M11 14l6 6 6-6" fill="none" stroke="#13a594" stroke-width="2.5"/></svg>
</section>

<section class="clients"><div class="wrap">
  <div class="label">Our clients</div>
  <p>We work with and represent a number of progressive companies in their SEO, social, inbound marketing, content and strategy needs. Check out our case-studies for examples.</p>
  <div class="logos">
    <div class="logo-tile"><i></i>Tradeloft</div>
    <div class="logo-tile"><i></i>CoachLive</div>
    <div class="logo-tile"><i></i>Wayfarer</div>
    <div class="logo-tile"><i></i>StayBook</div>
    <div class="logo-tile" style="color:#222;font-size:17px;line-height:1.1;text-align:center">Image<br>coming<br>soon</div>
  </div>
</div></section>

<section class="cta">
  <div class="label">Sound interesting?</div>
  <h2>Interested in what you have seen so far?</h2>
  <p>Are you looking for a progressive and innovative inbound marketing agency who can work alongside your existing teams. If Yes, then let's have a chat.</p>
  <a class="btn" href="#">Contact us</a>
</section>

<section class="contact">
  <svg class="chevron" style="top:-17px;bottom:auto" viewBox="0 0 34 34"><circle cx="17" cy="17" r="16" fill="#fff" stroke="#13a594" stroke-width="2"/><path d="M11 20l6-6 6 6" fill="none" stroke="#13a594" stroke-width="2.5"/></svg>
  <div class="wrap">
    <span class="label">Contact</span>
    <h2 class="heading">Where are we?</h2>
    <p class="lede">We are in London, UK, based down the best mews in Little Venice, so come check it out and walk the canals with us, we're happy to welcome you.</p>
    <div class="grid">
      <div><h3>UK Office</h3><p class="small">14 Harrow Lane, Little Venice,<br>London, UK, W9 1XX</p></div>
      <div><h3>Phone</h3><p class="val">+44 (0) 20 7946 0321</p></div>
      <div><h3>Email</h3><p class="val">hello@trovalink.co.uk</p></div>
      <div><h3>Connect with us</h3><div class="social"><i></i><i></i><i></i><i></i></div></div>
      <div style="border-bottom:0"><h3>Useful links</h3><ul><li>Home</li><li>About</li><li>Portfolio</li><li>What we do</li><li>Contact us</li></ul></div>
      <div style="border-bottom:0;grid-column:span 2;padding-right:60px"><h3>About us</h3><p class="small">Trovalink is an inbound marketing agency offering a raft of services from digital strategy and planning through to SEO, Social media, SMM, CRO, Design &amp; Creative, through to paid for performance campaigns.</p><p class="small" style="margin-top:10px">Talk to us to discuss your needs.</p></div>
      <div style="border-bottom:0" class="search"><h3>Search this site</h3><input type="text" placeholder="Search"><br><a class="btn" href="#">Search</a></div>
    </div>
  </div>
</section>

<footer class="site-footer"><div class="wrap">
  <div class="brand">TROVALINK</div>
  <p>COPYRIGHT (C) 2013 TROVALINK. ALL RIGHTS RESERVED.<br>Trovalink is the trading name of Trovalink Limited, registered in the UK at Companies House 06112233.</p>
</div></footer>

</body>
</html>
```